Graphic Design Project

We make rose petal jelly from old fashioned english roses. The jelly is sweet eaten with scones and clotted cream or as a filling in a victoria sandwich, as a topping on ice cream or thick set yogurt.
The image of the product is luxurious and decadent and very english.
We need a design for a label which has a picture of an old fashioned rose (rosa mundi or a compte de chambard) The rose must stand out clearly so the jelly is not confused with other fruit jams. The overall colour of the label should be pink and soft, with white or dark pink writing. The label needs to be fridge proof.

We also need a security strip to fit on the lid of the jar.

We need the following information on the label.
Name of our company-"Meadow Lantern"
Name of Product-"Rose Petal Jelly"
Sales pitch-"With whole petals-a taste of summer, delicious on scones, as a filling in sponge cake, as a topping on ice cream or yogurt."
INGREDIENTS: Sugar, water, rose petals, lemon juice, natural jelling agent (agar-agar)
STORAGE: Store in a cool dry place, once opened keep refrigerated and consume within 4 weeks.
BEST BEFORE: See base

200g
Produced by:
MEADOW LANTERN
The Larches
Brindle Lane
Newnham
Gloucestershire
GL17 4QX
The label must have room for a bar code. The size of label approx 8-10cm long 5cm wide.
Updates

Hi

Just been looking at the Harrowgate and Pellow site and the labels they have there have the up market feel I am trying to convey. Hope that helps, its classy but not twee.

Thanks

Thanks for all submissions. I would be grateful if you googled images for 'Colourful and expensive biscuits at Harrowgate Pellow' The designs on the tins are the image we are trying to create. The colours are quite strong.

Thanks

Target Market(s)

older well off people who visit garden centres

Industry/Entity Type

Security

Requirements
Must have
• All writen info above and picture of old fashioned rose prferably rose a mundi. Luxury feel, very english, to appeal to older market
Pink colour sheme
Should not have
• dark or manly colours

```html
<!DOCTYPE html>
<html lang="en">
<head>
<meta charset="utf-8">
<title>Meadow Lantern – Rose Petal Jelly Security Strips</title>
<link rel="stylesheet" href="https://fonts.googleapis.com/css2?family=Cinzel:wght@500&display=swap">
<style>
  :root {
    --paper: #ffffff;
    --rose-soft: #f59dac;
    --rose-strong: #f2719a;
    --rule: #ffffff;
    --lettering: #ffffff;
  }
  html, body {
    margin: 0;
    padding: 0;
    width: 1200px;
    height: 380px;
    overflow: hidden;
    background: var(--paper);
  }
  .strip-sheet {
    display: block;
    width: 1200px;
    height: 380px;
  }
  .band--soft { fill: var(--rose-soft); }
  .band--strong { fill: var(--rose-strong); }
  .band-rule { fill: var(--rule); }
  .strip-title {
    font-family: "Cinzel", "Times New Roman", serif;
    font-weight: 500;
    font-size: 40px;
    fill: var(--lettering);
  }
</style>
</head>
<body>
<svg class="strip-sheet" viewBox="0 0 1200 380" xmlns="http://www.w3.org/2000/svg" aria-label="Two lid security strips for Meadow Lantern Rose Petal Jelly">
  <g class="security-strip security-strip--soft">
    <rect class="band band--soft" x="0" y="26" width="1200" height="127"/>
    <rect class="band-rule" x="0" y="37" width="1200" height="4"/>
    <rect class="band-rule" x="0" y="137" width="1200" height="4"/>
    <text class="strip-title" x="600" y="101" text-anchor="middle" textLength="1044" lengthAdjust="spacing">MEADOW LANTERN • ROSE PETAL JELLY</text>
  </g>
  <g class="security-strip security-strip--strong">
    <rect class="band band--strong" x="0" y="230" width="1200" height="128"/>
    <rect class="band-rule" x="0" y="242" width="1200" height="4"/>
    <rect class="band-rule" x="0" y="340" width="1200" height="4"/>
    <text class="strip-title" x="600" y="305" text-anchor="middle" textLength="1044" lengthAdjust="spacing">MEADOW LANTERN • ROSE PETAL JELLY</text>
  </g>
</svg>
</body>
</html>
```